Design a cover for a book called The Quiet Harvest

Describe a cover for a 5.5" x 8.5" 200-page paperback book titled The Quiet Harvest. The subtitle is: A Civic Field Manual for Shaping a Country Where Families Can Thrive Together

The book is about how we can change our economic system to provide universal basic income, free healthcare, and free college while also lowering our tax rates. The book is uplifting, talks about the spiritual growth our society will need in positive terms. The website TheCommonLedgerPlan.example will be used to promote the book, and is a good resources for design ideas.

Target Market(s)

Economics, Finance, Spiritual

Font styles to use
Serif
Sans Serif

Colors

Designer to choose colors to be used in the design.

Requirements
Must have
• Include the URL on the back cover: TheQuietHarvest.example
Include the attached ISBN Barcode on the back cover
Include the title on the front cover: The Quiet Harvest
Include the subtitle on the front cover: A Civic Field Manual for Shaping a Country Where Families Can Thrive Together
Include the author's name Martin Lowell Perry on the front cover

Here is the size of the cover:
Spine Width 0.4504” (200 x 0.002252”)
Full Width 11.7004” (0.125 + 5.5 + 0.4504 + 5.5 +0.125) 3511 pixels @300DPI
Full Height 8.75” (0.125 + 8.5 + 0.125) 2625 pixels @ 300DPI

```html
<!DOCTYPE html>
<html lang="en">
<head>
<meta charset="utf-8">
<title>The Quiet Harvest — Book Cover</title>
<link rel="stylesheet" href="https://fonts.googleapis.com/css2?family=Bebas+Neue&family=Montserrat:wght@500;600&display=swap">
<style>
  :root {
    --page-bg: #ececec;
    --cover-bg: #fdfdfc;
    --ink: #111111;
    --orange-deep: #e07a2e;
    --orange-light: #f8bd4f;
    --field-sky: #f4f3ee;
    --field-mid: #a9a489;
    --field-grass: #6f7a3c;
    --bill-tone: #c9cdbd;
  }
  * { margin: 0; padding: 0; box-sizing: border-box; }
  html, body {
    width: 1200px; height: 857px; overflow: hidden;
    background: var(--page-bg);
  }
  .cover {
    position: absolute;
    left: 380px; top: 88px;
    width: 440px; height: 681px;
    background: var(--cover-bg);
    overflow: hidden;
  }
  .title-small {
    position: absolute; top: 38px; left: 0; width: 100%;
    text-align: center;
    font-family: "Montserrat", sans-serif; font-weight: 600;
    font-size: 24px; letter-spacing: 5px; color: var(--ink);
  }
  .title-main {
    position: absolute; left: 0; width: 100%;
    text-align: center;
    font-family: "Bebas Neue", sans-serif;
    font-size: 130px; line-height: 1; letter-spacing: 1px;
  }
  .title-main.line-one { top: 76px; color: var(--ink); }
  .title-main.line-two {
    top: 177px;
    background: linear-gradient(90deg, var(--orange-deep) 0%, var(--orange-light) 50%, var(--orange-deep) 100%);
    -webkit-background-clip: text; background-clip: text;
    color: transparent;
  }
  .bill {
    position: absolute; width: 58px; height: 32px;
    background: var(--bill-tone); border-radius: 3px;
  }
  .bill.top { left: 350px; top: 8px; transform: rotate(22deg); }
  .bill.left { left: 52px; top: 150px; transform: rotate(70deg); }
  .bill.right { left: 262px; top: 252px; transform: rotate(-28deg); }
  .subtitle {
    position: absolute; top: 344px; left: 0; width: 100%;
    text-align: center;
    font-family: "Montserrat", sans-serif; font-weight: 600;
    font-size: 17.5px; line-height: 24px; color: var(--ink);
    text-transform: uppercase;
  }
  .crowd-photo {
    position: absolute; left: 0; top: 418px; width: 100%; height: 185px;
    background: linear-gradient(180deg, var(--cover-bg) 0%, var(--field-sky) 20%, var(--field-mid) 65%, var(--field-grass) 100%);
  }
  .author-band {
    position: absolute; left: 0; top: 603px; width: 100%; height: 78px;
    background: linear-gradient(90deg, var(--orange-deep) 0%, var(--orange-light) 50%, var(--orange-deep) 100%);
    display: flex; align-items: center; justify-content: center;
  }
  .author-name {
    font-family: "Bebas Neue", sans-serif;
    font-size: 52px; line-height: 1; color: #ffffff; padding-top: 4px;
  }
</style>
</head>
<body>
  <main class="cover">
    <div class="title-small">THE</div>
    <div class="title-main line-one">QUIET</div>
    <div class="title-main line-two">HARVEST</div>
    <div class="bill top" role="img" aria-label="Floating banknote"></div>
    <div class="bill left" role="img" aria-label="Floating banknote"></div>
    <div class="bill right" role="img" aria-label="Floating banknote"></div>
    <p class="subtitle">A Civic Field Manual for Shaping<br>a Country Where Families<br>Can Thrive Together</p>
    <div class="crowd-photo" role="img" aria-label="Photograph of a diverse group of people seen from behind, standing in a sunlit grassy field"></div>
    <div class="author-band"><span class="author-name">MARTIN LOWELL PERRY</span></div>
  </main>
</body>
</html>
```